Q-VIRO STATIONERY
Q-VIRO Stationery
Project: Q-VIRO STATIONERY
Q-VIRO STATIONERY - Construction
Creative Brief
Simple
KL MARLOW
5172 HOLLOWAY LANE EAST POINT GEORGA 303044
Kl@q-viroco.example

```html
<!DOCTYPE html>
<html lang="en">
<head>
<meta charset="utf-8">
<title>Q-VIRO Stationery</title>
<link href="https://fonts.googleapis.com/css2?family=Michroma&family=Roboto:wght@400;500&display=swap" rel="stylesheet">
<style>
  :root {
    --stage: #8d8d8d;
    --card: #ffffff;
    --ink: #2f3338;
    --muted: #4a4f55;
    --blue-deep: #1d3fd1;
    --blue-mid: #2f6bff;
    --blue-light: #6fb2ff;
    --charcoal: #3b3e42;
  }
  * { box-sizing: border-box; margin: 0; padding: 0; }
  html, body { width: 1200px; height: 901px; overflow: hidden; }
  body {
    background: var(--stage);
    font-family: "Roboto", Arial, sans-serif;
    display: flex;
    flex-direction: column;
    align-items: center;
    justify-content: center;
    gap: 56px;
  }
  .card {
    position: relative;
    width: 640px;
    height: 366px;
    background: var(--card);
    overflow: hidden;
    box-shadow: 0 6px 18px rgba(0,0,0,0.25);
  }

  /* Front */
  .brand-name {
    position: absolute;
    left: 40px;
    top: 96px;
    font-family: "Michroma", "Arial Black", sans-serif;
    font-size: 44px;
    line-height: 60px;
    color: var(--ink);
    letter-spacing: 1px;
  }
  .brand-circle {
    position: absolute;
    right: 46px;
    top: 38px;
    width: 170px;
    height: 170px;
    border-radius: 50%;
    background: var(--blue-mid);
  }
  .name-band {
    position: absolute;
    left: 0;
    top: 168px;
    width: 66%;
    height: 34px;
    background: linear-gradient(90deg, var(--blue-light) 0%, var(--blue-mid) 45%, var(--blue-deep) 100%);
  }
  .person-name {
    position: absolute;
    left: 40px;
    top: 168px;
    font-size: 19px;
    line-height: 34px;
    font-weight: 500;
    color: #ffffff;
    letter-spacing: 1px;
  }
  .address {
    position: absolute;
    left: 40px;
    top: 222px;
    font-size: 12px;
    line-height: 16px;
    color: var(--muted);
    text-transform: uppercase;
  }
  .contacts {
    position: absolute;
    left: 296px;
    top: 216px;
    list-style: none;
    font-size: 12px;
    line-height: 19px;
    color: var(--muted);
  }
  .contacts li { display: flex; align-items: center; gap: 7px; }
  .contacts svg { width: 11px; height: 11px; fill: var(--blue-deep); }

  /* Back */
  .back-band {
    position: absolute;
    left: 0;
    top: 258px;
    width: 100%;
    height: 18px;
    background: linear-gradient(90deg, var(--blue-light) 0%, var(--blue-mid) 35%, var(--blue-deep) 62%, transparent 62%);
  }
  .back-bar {
    position: absolute;
    right: 0;
    top: 200px;
    width: 140px;
    height: 18px;
    background: var(--charcoal);
  }
  .back-brand {
    position: absolute;
    left: 410px;
    top: 226px;
    display: flex;
    align-items: center;
    gap: 8px;
  }
  .back-brand .dot {
    width: 22px; height: 22px; border-radius: 50%;
    background: var(--blue-mid);
  }
  .back-brand span {
    font-family: "Michroma", "Arial Black", sans-serif;
    font-size: 22px;
    color: var(--ink);
  }
</style>
</head>
<body>
  <section class="card card-front">
    <div class="brand-name">Q-VIRO</div>
    <div class="brand-circle"></div>
    <div class="name-band"></div>
    <div class="person-name">KL MARLOW</div>
    <p class="address">5172 Holloway Lane<br>Larkspur Vale<br>Nevada 89901</p>
    <ul class="contacts">
      <li><svg viewBox="0 0 12 12"><path d="M3 1l2 2.5-1.2 1.2a7 7 0 0 0 3.5 3.5L8.5 7 11 9l-1.5 2C5 11 1 7 1 2.5z"/></svg>555-010-0142</li>
      <li><svg viewBox="0 0 12 12"><rect x="1" y="3" width="10" height="7" rx="1"/><rect x="3" y="1" width="6" height="3"/></svg>555-010-0187</li>
      <li><svg viewBox="0 0 12 12"><path d="M1 2h10v8H1z"/></svg>Kl@q-viroco.example</li>
    </ul>
  </section>

  <section class="card card-back">
    <div class="back-bar"></div>
    <div class="back-brand"><div class="dot"></div><span>Q-VIRO</span></div>
    <div class="back-band"></div>
  </section>
</body>
</html>
```